Flyer to acquire new customers for a craft business

Create an A5 (4 pages in total) flyer describing proposed services from a craft business to new customers.

Services are :

All types of renovation (painting, plastering, attaching wallpapers ....)
All types of repairs
Electric repairs
Little to medium woodworks
Services around the house and garden

Flyer must be translatable into several languages beginning with FRENCH.
Texts are being written by ourselves.

Target Market(s)

Private customers

Industry/Entity Type

Mixed craft business

Colors

Designer to choose colors to be used in the design.

```html
<!DOCTYPE html>
<html lang="fr">
<head>
<meta charset="utf-8">
<title>Handwierk Plus – Flyer</title>
<link href="https://fonts.googleapis.com/css2?family=Arimo:wght@400;700&display=swap" rel="stylesheet">
<style>
  :root {
    --navy: #1f1a3b;
    --plum: #22183a;
    --yellow: #fbb53c;
    --lavender: #e2e4ee;
    --steel: #8a93b5;
    --grey-line: #9aa1bb;
    --ink: #23203a;
    --white: #ffffff;
    --backdrop: #dcdcdc;
  }
  html, body { margin: 0; padding: 0; }
  body {
    width: 1200px; height: 1200px; overflow: hidden;
    background: var(--backdrop);
    font-family: "Arimo", Arial, sans-serif;
    position: relative;
  }
  .sheet { position: absolute; width: 677px; height: 478px; overflow: hidden; }
  .sheet--cover { left: 98px; top: 89px; }
  .sheet--services { left: 437px; top: 630px; }
  .sheet__inner {
    position: absolute; left: 0; top: 0;
    width: 1090px; height: 770px;
    transform: scale(0.6211); transform-origin: 0 0;
    background: var(--white); overflow: hidden;
  }
  .sheet__art { position: absolute; inset: 0; width: 1090px; height: 770px; }
  .hex-fill { stroke-linejoin: round; stroke-width: 10; }
  .hex-line { fill: none; stroke-linejoin: round; stroke-width: 2; }
  .abs { position: absolute; margin: 0; }

  .brand { display: flex; align-items: center; gap: 14px; color: var(--navy); font-weight: 700; font-size: 26px; }
  .brand__dot { width: 80px; height: 80px; border-radius: 50%; background: var(--navy); flex: none; }
  .brand--top { left: 587px; top: 44px; }
  .brand--bottom { left: 52px; top: 468px; font-size: 24px; }
  .brand--bottom .brand__dot { width: 72px; height: 72px; }

  .cover-title {
    left: 608px; top: 160px; font-size: 50px; line-height: 58px; font-weight: 700; color: var(--navy);
    transform: rotate(-7deg); transform-origin: 0 100%; white-space: nowrap;
  }
  .contact { left: 55px; top: 598px; color: var(--ink); font-style: normal; }
  .contact__name { font-size: 19px; font-weight: 700; margin: 0 0 10px; }
  .contact__list { list-style: none; margin: 0; padding: 0; font-size: 15px; }
  .contact__list li { display: flex; align-items: center; gap: 10px; height: 23.3px; }
  .contact__list svg { width: 13px; height: 13px; flex: none; }

  .service-title { font-size: 19px; font-weight: 400; margin: 0; }
  .service-title--gold { color: var(--yellow); }
  .service-title--steel { color: var(--steel); }
  .service-list { list-style: none; margin: 6px 0 0; padding: 0; font-size: 13px; line-height: 15.5px; }
  .service-list li { position: relative; padding-left: 13px; margin-bottom: 8px; }
  .service-list li::before { content: "•"; position: absolute; left: 0; color: var(--yellow); }
  .service-list li.cont::before { content: ""; }
  .on-dark { color: var(--white); }
  .on-dark .service-list li::before { color: var(--steel); }
  .on-light { color: var(--ink); }

  .block--renovation { left: 246px; top: 70px; width: 240px; }
  .block--electric { left: 37px; top: 564px; width: 195px; }
  .block--repairs { left: 284px; top: 534px; width: 225px; }

  .headline { left: 599px; top: 60px; width: 255px; color: var(--yellow); font-size: 31px; font-weight: 700; line-height: 39px; }
  .pitch { left: 599px; top: 553px; width: 460px; color: var(--ink); font-size: 20.5px; line-height: 26px; }
  .pitch p { margin: 0 0 11px; }
</style>
</head>
<body>

<section class="sheet sheet--cover">
  <div class="sheet__inner">
    <svg class="sheet__art" viewBox="0 0 1090 770">
      <defs>
        <linearGradient id="grinderTone" x1="0" y1="0" x2="1" y2="1">
          <stop offset="0" stop-color="#2b3136"/>
          <stop offset="0.5" stop-color="#4d5a5c"/>
          <stop offset="0.8" stop-color="#5a3a20"/>
          <stop offset="1" stop-color="#1c1e22"/>
        </linearGradient>
      </defs>
      <polygon class="hex-line" stroke="var(--yellow)" points="138,46 297,138 297,322 138,414 -21,322 -21,138"/>
      <polygon class="hex-fill" fill="var(--lavender)" stroke="var(--lavender)" points="329,138 440,202 440,330 329,394 218,330 218,202"/>
      <polygon class="hex-line" stroke="var(--grey-line)" points="110,301 360,445 360,735 110,879 -140,735 -140,445"/>
      <polygon class="hex-fill" fill="var(--yellow)" stroke="var(--yellow)" points="439,66 479,89 479,135 439,158 399,135 399,89"/>
      <polygon class="hex-line" stroke="var(--navy)" points="418,262 482,299 482,373 418,410 354,373 354,299"/>
      <polygon class="hex-line" stroke="var(--yellow)" points="582,334 746,429 746,618 582,712 418,618 418,429"/>
      <polygon class="hex-line" stroke="var(--grey-line)" points="922,213 1156,348 1156,618 922,753 688,618 688,348"/>
      <polygon class="hex-fill" fill="var(--lavender)" stroke="var(--lavender)" points="900,240 1120,367 1120,620 900,747 680,620 680,367"/>
      <polygon class="hex-fill" fill="url(#grinderTone)" stroke="url(#grinderTone)" role="img" aria-label="Photo : artisan utilisant une meuleuse d'angle avec gerbe d'étincelles" points="862,256 1087,386 1087,641 862,771 642,641 642,386"/>
      <polygon class="hex-line" stroke="var(--grey-line)" points="830,340 1055,470 1055,730 830,860 605,730 605,470"/>
      <polygon class="hex-fill" fill="var(--yellow)" stroke="var(--yellow)" points="714,248 764,277 764,333 714,362 664,333 664,277"/>
      <polygon class="hex-fill" fill="#b9b9bd" stroke="#b9b9bd" opacity="0.85" points="1007,434 1065,467 1065,535 1007,568 949,535 949,467"/>
      <polygon class="hex-fill" fill="var(--yellow)" stroke="var(--yellow)" opacity="0.55" points="814,587 864,616 864,672 814,701 764,672 764,616"/>
      <polygon class="hex-fill" fill="#cfcfd3" stroke="#cfcfd3" opacity="0.9" points="1042,657 1093,687 1093,745 1042,775 991,745 991,687"/>

      <line x1="760" y1="133" x2="1052" y2="98" stroke="var(--steel)" stroke-width="4"/>
      <line x1="650" y1="154" x2="807" y2="139" stroke="var(--yellow)" stroke-width="3"/>
      <line x1="579" y1="228" x2="872" y2="193" stroke="var(--navy)" stroke-width="3"/>

      <polygon class="hex-fill" fill="var(--yellow)" stroke="var(--yellow)" points="407,683 420,691 420,707 407,715 394,707 394,691"/>
      <polygon class="hex-fill" fill="var(--yellow)" stroke="var(--yellow)" points="452,683 465,691 465,707 452,715 439,707 439,691"/>
    </svg>

    <div class="abs brand brand--top"><span class="brand__dot"></span><span>Handwierk Plus</span></div>
    <h1 class="abs cover-title">Aren Handwierker</h1>
    <div class="abs brand brand--bottom"><span class="brand__dot"></span><span>Handwierk Plus</span></div>

    <address class="abs contact">
      <p class="contact__name">Handwierk Plus</p>
      <ul class="contact__list">
        <li><svg viewBox="0 0 12 12"><path d="M6 0.5a4 4 0 0 0-4 4c0 3 4 7 4 7s4-4 4-7a4 4 0 0 0-4-4zm0 5.6a1.6 1.6 0 1 1 0-3.2 1.6 1.6 0 0 1 0 3.2z" fill="var(--steel)"/></svg>12, rue des Artisans, 4321 Beispilldorf</li>
        <li><svg viewBox="0 0 12 12"><path d="M2.5 0.8l2 2-1 1.5c.7 1.6 2 2.9 3.6 3.6l1.5-1 2 2-1.3 1.9C5 10.5 1.5 7 1 2.1z" fill="var(--steel)"/></svg>20 00 12 34</li>
        <li><svg viewBox="0 0 12 12"><circle cx="6" cy="6" r="5" fill="none" stroke="var(--steel)" stroke-width="1.2"/><path d="M1 6h10M6 1c-2.5 3-2.5 7 0 10M6 1c2.5 3 2.5 7 0 10" fill="none" stroke="var(--steel)" stroke-width="1"/></svg>www.handwierkplus.lu</li>
        <li><svg viewBox="0 0 12 12"><rect x="0.5" y="2.5" width="11" height="7" fill="var(--steel)"/><path d="M0.5 2.5l5.5 4 5.5-4" fill="none" stroke="var(--white)" stroke-width="1"/></svg>contact@handwierkplus.lu</li>
      </ul>
    </address>
  </div>
</section>

<section class="sheet sheet--services">
  <div class="sheet__inner">
    <svg class="sheet__art" viewBox="0 0 1090 770">
      <defs>
        <linearGradient id="brushTone" x1="0" y1="0" x2="1" y2="1">
          <stop offset="0" stop-color="#c98b4b"/><stop offset="0.5" stop-color="#e8a53a"/><stop offset="1" stop-color="#e9e6e2"/>
        </linearGradient>
        <linearGradient id="toolTone" x1="0" y1="0" x2="1" y2="1">
          <stop offset="0" stop-color="#1d2126"/><stop offset="0.5" stop-color="#8a8c8e"/><stop offset="0.75" stop-color="#e7c53a"/><stop offset="1" stop-color="#22262b"/>
        </linearGradient>
        <linearGradient id="wireTone" x1="0" y1="0" x2="1" y2="1">
          <stop offset="0" stop-color="#e4d6a0"/><stop offset="0.5" stop-color="#d9dadc"/><stop offset="1" stop-color="#3c8fd0"/>
        </linearGradient>
        <linearGradient id="woodTone" x1="0" y1="0" x2="1" y2="1">
          <stop offset="0" stop-color="#b57a52"/><stop offset="0.5" stop-color="#d7a07a"/><stop offset="1" stop-color="#8f5a3b"/>
        </linearGradient>
      </defs>
      <polygon fill="var(--plum)" points="0,0 1090,0 1090,85 450,462 0,263"/>
      <polygon class="hex-line" stroke="var(--yellow)" points="335,-19 519,87 519,299 335,405 151,299 151,87"/>
      <polygon class="hex-line" stroke="var(--grey-line)" points="129,457 257,531 257,679 129,753 1,679 1,531"/>
      <polygon class="hex-fill" fill="url(#brushTone)" stroke="url(#brushTone)" role="img" aria-label="Photo : pinceaux, rouleaux et gants de peinture" points="129,41 215,91 215,189 129,239 43,189 43,91"/>
      <polygon class="hex-fill" fill="url(#toolTone)" stroke="url(#toolTone)" role="img" aria-label="Photo : main tenant des clés et une pince" points="165,258 287,329 287,468 165,538 43,468 43,329"/>
      <polygon class="hex-fill" fill="url(#wireTone)" stroke="url(#wireTone)" role="img" aria-label="Photo : matériel électrique, câbles et rubans isolants" points="367,333 445,378 445,468 367,513 289,468 289,378"/>
      <polygon class="hex-fill" fill="var(--yellow)" stroke="var(--yellow)" points="454,439 490,460 490,500 454,521 418,500 418,460"/>
      <polygon class="hex-fill" fill="#c5cadf" stroke="#c5cadf" opacity="0.85" points="734,260 843,323 843,447 734,510 625,447 625,323"/>
      <polygon class="hex-fill" fill="url(#woodTone)" stroke="url(#woodTone)" role="img" aria-label="Photo : pile de planches de bois" points="898,144 1059,237 1059,421 898,514 737,421 737,237"/>
      <polygon class="hex-line" stroke="var(--white)" points="909,187 1063,276 1063,454 909,543 755,454 755,276"/>
      <polygon class="hex-fill" fill="var(--yellow)" stroke="var(--yellow)" points="988,81 1024,102 1024,142 988,163 952,142 952,102"/>
    </svg>

    <div class="abs block--renovation on-dark">
      <h2 class="service-title service-title--gold">Rénovations</h2>
      <ul class="service-list">
        <li>Nous proposons tous types de rénovations (petite. moyenne ou grande envergure)</li>
        <li>Peinture. carrelage. plâtrage. murs en placo-plâtre. sanitaire</li>
        <li style="margin-bottom:6px">Nous utilisons des produits standards</li>
        <li class="cont">bien connus mais de méme des produits naturels comme l'argile et bien d'autres</li>
      </ul>
    </div>

    <div class="abs block--electric on-light">
      <h2 class="service-title service-title--steel">Travaux en électricité</h2>
      <ul class="service-list">
        <li>Installation de lampadaires. remplacements et extensions de circuits électriques. dépannages en électricité. systémes d'alarme et de vidéosurveillance ne sont quelques exemples de notre savoir faire</li>
      </ul>
    </div>

    <div class="abs block--repairs on-light">
      <h2 class="service-title service-title--steel">Réparations</h2>
      <ul class="service-list">
        <li>Une fuite d'eau ? un remplacement d'un tuyau ou méme une extension sanitaire ?</li>
        <li>Remplacer du carrelage défectueux méme des petits travaux ?</li>
        <li>Une réparation d'un garde-corps ? Le remplacement d'une porte intérieure ?</li>
        <li>Presque tout est possible !</li>
      </ul>
    </div>

    <h2 class="abs headline">Vous étes à la recherche d'un partenaire fiable ?</h2>

    <div class="abs pitch">
      <p>Pour tous types de travaux et de services de l'artisanat.</p>
      <p>Petits, moyens et aussi plus grands.</p>
      <p>Intervention rapide.</p>
      <p>Contactez-nous pour un conseil personnalisé.</p>
    </div>
  </div>
</section>

</body>
</html>
```